ashby paving works

Needs to have phone number 0412885107 and email marklowry@pavemail.com.au.
ABN 27613048852
name mark lowry

For all your concreting solutions
Excavation
Exposed & colour concrete
House & shed slabs
Driveways
Landing & steps

Contact Information for Business Card

ph 0412885107
email marklowry@pavemail.com.au.
ABN 27613048852
name mark lowry

```html
<!DOCTYPE html>
<html lang="en">
<head>
<meta charset="utf-8">
<title>Ashby Paving Works – Business Card</title>
<link rel="stylesheet" href="https://fonts.googleapis.com/css2?family=Barlow:wght@500;600;700&display=swap">
<style>
  :root {
    --orange: #e8652f;
    --grey: #6b625c;
    --peach: #f4a98a;
    --faint: #f8e6dc;
    --white: #ffffff;
    --band-text: #f6d3c0;
  }
  * { margin: 0; padding: 0; box-sizing: border-box; }
  html, body { width: 1200px; height: 2406px; overflow: hidden; }
  body { position: relative; background: var(--white); font-family: "Barlow", Arial, sans-serif; }

  .backdrop { position: absolute; left: 0; top: 0; width: 1200px; height: 995px; background: var(--peach); }

  .card { position: absolute; left: 0; width: 1200px; background: var(--white); overflow: hidden; }
  .card--front { top: 995px; height: 705px; }
  .card--back { top: 1700px; height: 706px; }

  .front-shapes { position: absolute; inset: 0; }

  .brand-mark {
    position: absolute; display: flex; align-items: center; gap: 14px;
    color: var(--white); font-weight: 700; letter-spacing: 1px;
  }
  .brand-mark__square { width: 26px; height: 26px; background: currentColor; flex: none; }
  .card--front .brand-mark { left: 40px; top: 290px; font-size: 34px; line-height: 1.05; }

  .company { position: absolute; left: 556px; top: 212px; width: 560px; text-align: center; }
  .company__name { color: var(--orange); font-weight: 700; font-size: 42px; line-height: 1; letter-spacing: 0.5px; }
  .company__sub {
    display: flex; align-items: center; justify-content: center; gap: 14px;
    color: var(--grey); font-weight: 500; font-size: 32px; letter-spacing: 6px; line-height: 1; margin-top: 2px;
  }
  .company__sub::before, .company__sub::after { content: ""; width: 100px; height: 3px; background: var(--grey); }
  .company__abn { color: var(--orange); font-weight: 700; font-size: 28px; letter-spacing: 1.5px; margin-top: 8px; }

  .person { position: absolute; left: 746px; top: 380px; color: var(--orange); font-weight: 700; font-size: 46px; letter-spacing: 1.5px; }

  .contact { position: absolute; left: 746px; display: flex; align-items: center; gap: 12px; color: var(--grey); font-weight: 700; }
  .contact--phone { top: 462px; font-size: 26px; letter-spacing: 3px; }
  .contact--email { top: 526px; font-size: 23px; }
  .contact svg { flex: none; }

  .card--back .brand-mark {
    left: 0; right: 0; top: 150px; justify-content: center; color: var(--grey); font-size: 52px;
  }
  .card--back .brand-mark__square { width: 40px; height: 40px; background: var(--orange); }

  .tagline { position: absolute; left: 0; right: 0; top: 370px; text-align: center; color: var(--grey); font-weight: 700; font-size: 32px; letter-spacing: 2.5px; }

  .services { position: absolute; left: 0; top: 430px; width: 1200px; height: 276px; background: var(--orange); list-style: none; padding-top: 24px; }
  .services li {
    display: flex; align-items: center; justify-content: center; gap: 12px;
    color: var(--band-text); font-weight: 700; font-size: 30px; letter-spacing: 2.5px; line-height: 45px;
  }
  .services li::before, .services li::after { content: ""; width: 100px; height: 3px; background: var(--band-text); }
</style>
</head>
<body>
  <div class="backdrop"></div>

  <section class="card card--front">
    <svg class="front-shapes" width="1200" height="705" viewBox="0 0 1200 705">
      <polygon points="1000,5 1330,352 1000,700 670,352" fill="var(--faint)" opacity="0.8"/>
      <polygon points="0,0 329,0 481,705 0,705" fill="var(--orange)"/>
    </svg>

    <div class="brand-mark"><span class="brand-mark__square"></span><span>ASHBY<br>PAVING WORKS</span></div>

    <div class="company">
      <div class="company__name">ASHBY PAVING</div>
      <div class="company__sub">WORKS</div>
      <div class="company__abn">ABN&nbsp;&nbsp;27613048852</div>
    </div>

    <div class="person">Mark Lowry</div>

    <div class="contact contact--phone">
      <svg width="30" height="30" viewBox="0 0 30 30"><circle cx="15" cy="15" r="13" fill="none" stroke="var(--grey)" stroke-width="2.5"/><path d="M10.5 8.5l3 3-1.6 1.8c.8 1.8 2 3 3.8 3.8l1.8-1.6 3 3-1.8 1.8c-4.5-.6-9.4-5.5-10-10z" fill="var(--grey)"/></svg>
      <span>0412885107</span>
    </div>

    <div class="contact contact--email">
      <svg width="34" height="26" viewBox="0 0 34 26"><rect x="1" y="1" width="32" height="24" fill="var(--grey)"/><path d="M2 2l15 12L32 2" fill="none" stroke="var(--white)" stroke-width="2.5"/></svg>
      <span>marklowry@pavemail.com.au</span>
    </div>
  </section>

  <section class="card card--back">
    <div class="brand-mark"><span class="brand-mark__square"></span><span>ASHBY PAVING WORKS</span></div>
    <p class="tagline">For all your concreting solutions</p>
    <ul class="services">
      <li>Excavation</li>
      <li>Exposed &amp; colour concrete</li>
      <li>House &amp; shed slabs</li>
      <li>Driveways</li>
      <li>Landing &amp; steps</li>
    </ul>
  </section>
</body>
</html>
```